Fancy looking Inspection Postcard

Postcard needed for customers to inspect their product once it is delivered. We'll be giving them the steps for inspecting their product and to contact us if any issues arise. Would like to see something that sticks out but uses our company's colors. Would like to see creativity. Possibly utilizing the diamond steel background like we have in our logo.

Target Market(s)

Customers of our manufacturing shop

Industry/Entity Type

Manufacturing - metal wall art, custom products

Requirements
Must have
• our colors and logo
Nice to have
• get creative. i like creativity

```html
<!DOCTYPE html>
<html lang="en">
<head>
<meta charset="utf-8">
<title>Copper Ridge Works – Product Inspection Postcard</title>
<link rel="stylesheet" href="https://fonts.googleapis.com/css2?family=Poppins:wght@300;600;700&display=swap">
<style>
  :root {
    --salmon: #e38c79;
    --teal: #1d837e;
    --teal-dark: #1a7a78;
    --magenta: #d0188f;
    --magenta-deep: #bd1597;
    --ink-on-magenta: #2f7288;
  }
  * { margin: 0; padding: 0; box-sizing: border-box; }
  html, body { width: 802px; height: 1200px; overflow: hidden; }
  body {
    position: relative;
    background: var(--salmon);
    font-family: "Poppins", sans-serif;
  }

  /* Front of the postcard */
  .card-front {
    position: absolute; left: 0; top: 25px; width: 802px; height: 534px;
    background: var(--magenta);
  }
  .card-front__field {
    position: absolute; left: 23px; top: 0; width: 760px; height: 534px;
    background: var(--teal);
  }
  .brand-name {
    position: absolute; left: 0; right: 0; top: 255px;
    text-align: center;
    font-weight: 700; font-size: 22px; letter-spacing: 1px;
    color: var(--magenta);
  }

  /* Back of the postcard */
  .card-back {
    position: absolute; left: 2px; top: 602px; width: 800px; height: 534px;
    overflow: hidden;
  }
  .card-back__message {
    position: absolute; left: 0; top: 0; width: 376px; height: 534px;
    background: var(--teal);
  }
  .card-back__address {
    position: absolute; left: 376px; top: 0; width: 424px; height: 534px;
    background: linear-gradient(135deg, var(--magenta-deep), var(--magenta) 55%, var(--magenta-deep));
  }

  .guidelines-title {
    position: absolute; left: 47px; top: 66px;
    font-weight: 300; font-size: 17px; color: var(--salmon);
  }
  .step { position: absolute; left: 31px; width: 340px; height: 40px; }
  .step__number {
    position: absolute; left: 0; top: 0; width: 43px; height: 39px;
    border: 2px solid var(--magenta); border-radius: 4px;
    color: var(--magenta); font-weight: 700; font-size: 24px;
    line-height: 35px; text-align: center;
  }
  .step__title {
    position: absolute; left: 83px; top: 0;
    font-weight: 700; font-size: 15px; line-height: 18px;
    color: var(--magenta); white-space: nowrap;
  }
  .step__questions {
    position: absolute; left: 84px; top: 19px;
    font-weight: 700; font-size: 13.5px; line-height: 12.5px;
    color: var(--salmon); white-space: nowrap;
  }
  .step__questions--wide { font-size: 13px; letter-spacing: 1.3px; }

  .feedback-title {
    position: absolute; left: 49px; top: 396px;
    font-weight: 300; font-size: 16.5px; color: var(--salmon);
  }
  .feedback-text {
    position: absolute; left: 49px; top: 430px;
    font-weight: 300; font-size: 11.5px; line-height: 15px;
    color: var(--magenta); white-space: nowrap;
  }
  .feedback-contact { display: flex; align-items: center; gap: 4px; }
  .feedback-contact svg { flex: none; }
  .feedback-contact .gap { width: 10px; }

  .stamp-box {
    position: absolute; left: 261px; top: 94px; width: 110px; height: 110px;
    border: 1px solid var(--ink-on-magenta);
  }
  .address-line {
    position: absolute; right: 50px; height: 1px;
    background: var(--ink-on-magenta);
  }
  .contact-list { position: absolute; left: 202px; top: 428px; list-style: none; }
  .contact-list li {
    display: flex; align-items: center; height: 26px;
    font-weight: 300; font-size: 11.5px; color: var(--ink-on-magenta);
    white-space: nowrap;
  }
  .contact-icon {
    flex: none;
    width: 20px; height: 20px; margin-right: 13px;
    background: var(--teal); border-radius: 3px;
    display: flex; align-items: center; justify-content: center;
  }
</style>
</head>
<body>

<section class="card-front">
  <div class="card-front__field">
    <div class="brand-name">COPPER RIDGE WORKS</div>
  </div>
</section>

<section class="card-back">
  <div class="card-back__message">
    <h1 class="guidelines-title">PRODUCT INSPECTION GUIDELINES</h1>

    <div class="step" style="top:101px">
      <div class="step__number">1</div>
      <div class="step__title">Inspect General Shape</div>
      <div class="step__questions">Is it what you expected?<br>Is it bent or disoriented?</div>
    </div>
    <div class="step" style="top:163px">
      <div class="step__number">2</div>
      <div class="step__title">Inspect the welds if there are any</div>
      <div class="step__questions step__questions--wide">Do they look clean?<br>Are there any gaps?</div>
    </div>
    <div class="step" style="top:222px">
      <div class="step__number">3</div>
      <div class="step__title">Inspect the finish</div>
      <div class="step__questions">Are there any areas not finished?<br>Are the colors what you expected?</div>
    </div>
    <div class="step" style="top:282px">
      <div class="step__number">4</div>
      <div class="step__title">Check for functionality</div>
      <div class="step__questions">Does it work the way you want it to?<br>Is it what you expected?</div>
    </div>

    <h2 class="feedback-title">Did we do a good job?</h2>
    <div class="feedback-text">
      <p>If you think so, leave us a review on Reviewly.</p>
      <p>If not, Please let us know.</p>
      <p class="feedback-contact">
        <svg width="12" height="9" viewBox="0 0 12 9"><rect x="0.5" y="0.5" width="11" height="8" fill="var(--magenta)"/><path d="M0.5 0.5 L6 5 L11.5 0.5" fill="none" stroke="var(--teal)" stroke-width="1"/></svg>
        <span>info@crworks.com</span>
        <span class="gap"></span>
        <svg width="11" height="11" viewBox="0 0 24 24"><path fill="var(--magenta)" d="M6.6 10.8a15.2 15.2 0 0 0 6.6 6.6l2.2-2.2a1 1 0 0 1 1-.25 11.4 11.4 0 0 0 3.6.57 1 1 0 0 1 1 1V20a1 1 0 0 1-1 1A17 17 0 0 1 3 4a1 1 0 0 1 1-1h3.5a1 1 0 0 1 1 1c0 1.25.2 2.45.57 3.6a1 1 0 0 1-.25 1z"/></svg>
        <span>555-013-7720</span>
      </p>
    </div>
  </div>

  <div class="card-back__address">
    <div class="stamp-box"></div>
    <div class="address-line" style="top:252px; left:110px"></div>
    <div class="address-line" style="top:292px; left:94px"></div>
    <div class="address-line" style="top:326px; left:78px"></div>
    <div class="address-line" style="top:360px; left:62px"></div>

    <ul class="contact-list">
      <li><span class="contact-icon"><svg width="12" height="12" viewBox="0 0 24 24"><path fill="var(--salmon)" d="M6.6 10.8a15.2 15.2 0 0 0 6.6 6.6l2.2-2.2a1 1 0 0 1 1-.25 11.4 11.4 0 0 0 3.6.57 1 1 0 0 1 1 1V20a1 1 0 0 1-1 1A17 17 0 0 1 3 4a1 1 0 0 1 1-1h3.5a1 1 0 0 1 1 1c0 1.250.2 2.45.57 3.6a1 1 0 0 1-.25 1z"/></svg></span>(555) 014-2290</li>
      <li><span class="contact-icon"><svg width="12" height="9" viewBox="0 0 12 9"><rect x="0.5" y="0.5" width="11" height="8" fill="var(--salmon)"/><path d="M0.5 0.5 L6 5 L11.5 0.5" fill="none" stroke="var(--teal)" stroke-width="1"/></svg></span>orders@crworks.com</li>
      <li><span class="contact-icon"><svg width="12" height="12" viewBox="0 0 24 24"><g fill="none" stroke="var(--salmon)" stroke-width="2"><circle cx="12" cy="12" r="10"/><path d="M2 12h20M12 2c3 3 3 17 0 20M12 2c-3 3-3 17 0 20"/></g></svg></span>www.crworks.com/orders</li>
    </ul>
  </div>
</section>

</body>
</html>
```